Business car for dental practice

I have a new logo. Want it use for a new business card design. Hi end dental practice Would like a scan code on it for quick access to my web site and mobile site too. Green and purple are in logo design. Maybe have scan code on back? My website is peterhallwayDDS.example
Updates

Meadowlark Crest Dental Associates

482 N Tamarack Ln
Alder Bend, NY 12990
845-555-0173

367 W Corliss Dr. 
Suite 584
Fenwick Glen, NY 12991
845-555-0198

would like to incorporate logo, and addresses of both offices, and I recently saw a business card with a scan box on it which would bring people directly to the web site. if anyone knows how to do that, that could possibly go on the back of the card. (May be something I have to add at printing process) card can be one sided, or two sided.  

Reason: designer is revising for me. has not posted changes yet. hope he does soon!!

```html
<!DOCTYPE html>
<html lang="en">
<head>
<meta charset="utf-8">
<title>Meadowlark Crest Dental Associates — Business Card</title>
<link rel="stylesheet" href="https://fonts.googleapis.com/css2?family=Arimo:wght@400&display=swap">
<style>
  :root {
    --stage: #616163;
    --card: #ffffff;
    --card-edge: #d9d9d9;
    --band-top: #c83e9c;
    --band-bottom: #5a2c5a;
    --ink: #4a4a4a;
    --brand: #7a2e6e;
    --brand-mark: #8a3f80;
  }
  html, body {
    margin: 0;
    width: 1200px;
    height: 901px;
    overflow: hidden;
    background: var(--stage);
    font-family: "Arimo", Arial, sans-serif;
  }
  .stage {
    position: relative;
    width: 1200px;
    height: 901px;
  }
  .card {
    position: absolute;
    width: 520px;
    height: 298px;
    background: var(--card);
    border-radius: 26px;
    overflow: hidden;
    box-shadow: 0 6px 0 var(--card-edge), 0 10px 18px rgba(0,0,0,0.25);
  }
  .card--front { left: 70px; top: 150px; }
  .card--back  { left: 610px; top: 440px; }
  .card__band {
    position: absolute;
    top: 0;
    right: 0;
    width: 58px;
    height: 100%;
    background: linear-gradient(to bottom, var(--band-top), var(--band-bottom));
  }
  .brand {
    position: absolute;
    left: 60px;
    top: 129px;
    display: flex;
    align-items: center;
    gap: 12px;
  }
  .brand__square {
    width: 40px;
    height: 40px;
    background: var(--brand-mark);
    flex: none;
  }
  .brand__name {
    color: var(--brand);
    font-size: 19px;
    line-height: 1.15;
    white-space: nowrap;
  }
  .contact {
    position: absolute;
    left: 46px;
    top: 30px;
    color: var(--ink);
    font-size: 15px;
    line-height: 18px;
  }
  .contact p { margin: 0; }
  .contact__person { margin-bottom: 36px; }
  .contact__office + .contact__office { margin-top: 18px; }
</style>
</head>
<body>
<main class="stage">
  <section class="card card--front" aria-label="Card front">
    <div class="brand">
      <span class="brand__square" aria-hidden="true"></span>
      <span class="brand__name">Meadowlark Crest Dental Associates</span>
    </div>
    <div class="card__band"></div>
  </section>

  <section class="card card--back" aria-label="Card back">
    <div class="contact">
      <div class="contact__person">
        <p>Nolan Brack</p>
        <p>Dentist</p>
      </div>
      <div class="contact__office">
        <p>Meadowlark Crest Dental Associates</p>
        <p>482 N Tamarack Ln</p>
        <p>Alder Bend, NY 12990</p>
        <p>845-555-0173</p>
      </div>
      <div class="contact__office">
        <p>367 W Corliss Dr.</p>
        <p>Suite 584</p>
        <p>Fenwick Glen, NY 12991</p>
        <p>845-555-0198</p>
      </div>
    </div>
    <div class="card__band"></div>
  </section>
</main>
</body>
</html>
```